Popup Banners - BrightCounsel - Legal Technology

- We need two banners (same style) designed with two different images and different text.

- The details of the printing requirements are attached, along with suggested images.

- The banners should share the same theme as our website www.brightcounsel.com.au

- The first banner would include our logo (attached), use the 'roads join' image (attached) in some way and text: New Opportunities - Where legal services and technology meet.

- The second banner would include our logo (attached), use the 'jigsaw' image (attached) in some way and use text: Legal Technology Strategy, Advice and Capability.

- Details on what are required from the Printer is attached also.

Target Market(s)

Legal Professionals

Industry/Entity Type

Information Technology

Font styles to use
Sans Serif

Requirements
Must have
• Our logo (attached), suggested text and the image mentioned for each.
Nice to have
• Professional and modern look
Should not have
• Cheap looking

```html
<!DOCTYPE html>
<html lang="en">
<head>
<meta charset="utf-8">
<title>BrightCounsel – Popup Banners</title>
<link href="https://fonts.googleapis.com/css2?family=Open+Sans:wght@400;600;700&display=swap" rel="stylesheet">
<style>
  :root {
    --page-bg: #ffffff;
    --brand-blue: #2990ee;
    --band-line: #6fb6f4;
    --navy: #0c2657;
    --logo-grey: #4b4b4b;
    --logo-on-navy: #a7b1c4;
    --logo-accent: #6cc3f5;
    --text-light: #ffffff;
    --sky-top: #3f86d6;
    --sky-low: #a9c9e6;
    --grass-light: #7fbf3a;
    --grass-dark: #3f7e1f;
  }
  * { margin: 0; padding: 0; box-sizing: border-box; }
  html, body {
    width: 1200px; height: 1000px; overflow: hidden;
    background: var(--page-bg);
    font-family: "Open Sans", Arial, sans-serif;
  }
  .canvas { position: relative; width: 1200px; height: 1000px; }

  .banner { position: absolute; top: 0; height: 1000px; overflow: hidden; }
  .banner--opportunities { left: 153px; width: 408px; background: var(--brand-blue); }
  .banner--strategy { left: 634px; width: 407px; background: var(--navy); }

  .brand {
    position: absolute; display: flex; align-items: center; gap: 14px;
    color: var(--logo-grey); font-weight: 400; font-size: 30px; letter-spacing: 4px;
    white-space: nowrap;
  }
  .brand__mark { width: 22px; height: 22px; background: var(--logo-accent); flex: none; }
  .banner--opportunities .brand { left: 28px; top: 26px; }
  .banner--strategy .brand { left: 22px; top: 855px; color: var(--logo-on-navy); }

  .title-band {
    position: absolute; left: 0; top: 201px; width: 100%; height: 58px;
    border-top: 1px solid var(--band-line); border-bottom: 1px solid var(--band-line);
    color: var(--text-light); font-size: 34px; font-weight: 400;
    display: flex; align-items: center; justify-content: center;
  }

  .photo-roads {
    position: absolute; left: 0; top: 259px; width: 100%; height: 741px;
    background: linear-gradient(180deg, var(--sky-top) 0%, var(--sky-low) 17%, var(--grass-light) 20%, var(--grass-light) 45%, var(--grass-dark) 100%);
  }
  .photo-jigsaw {
    position: absolute; left: 0; top: 0; width: 100%; height: 420px;
    background:
      radial-gradient(ellipse at 65% 35%, #dfeeff 0%, #7fa9e0 22%, #2b4f95 50%, rgba(12,38,87,0) 80%),
      linear-gradient(180deg, #0e2450 0%, var(--navy) 100%);
  }

  .tagline {
    position: absolute; left: 0; width: 100%; text-align: center;
    color: var(--text-light); font-weight: 600; text-transform: uppercase;
  }
  .banner--opportunities .tagline { top: 680px; font-size: 31px; line-height: 38px; }
  .banner--strategy .tagline { top: 539px; font-size: 24px; line-height: 30px; }
</style>
</head>
<body>
<main class="canvas">
  <section class="banner banner--opportunities">
    <div class="brand"><span class="brand__mark"></span>BrightCounsel</div>
    <div class="photo-roads" role="img" aria-label="Photo of two dirt roads joining on a grassy hill under a blue sky"></div>
    <h2 class="title-band">NEW OPPORTUNITIES</h2>
    <p class="tagline">Where legal services<br>and technology meet</p>
  </section>

  <section class="banner banner--strategy">
    <div class="photo-jigsaw" role="img" aria-label="Photo of a hand placing a glowing jigsaw piece into a blue puzzle"></div>
    <p class="tagline">Legal technology strategy<br>advice and capability</p>
    <div class="brand"><span class="brand__mark"></span>BrightCounsel</div>
  </section>
</main>
</body>
</html>
```